landscaping core flute signs

I need core flutes created with business name and a few extra dot points for putting on fences for job sites 120cm x 120cm approx.
I want our old ones information with the new L logo and colour palette

```html
<!DOCTYPE html>
<html lang="en">
<head>
<meta charset="utf-8">
<title>Terrace Ridge – Job Site Sign</title>
<link href="https://fonts.googleapis.com/css2?family=Poppins:wght@500;700;800&display=swap" rel="stylesheet">
<style>
  :root {
    --page: #cfcfcf;
    --stone-light: #f1f1f1;
    --stone-mid: #e2e2e2;
    --green: #5e8a55;
    --black: #0b0b0b;
    --white: #ffffff;
  }
  * { box-sizing: border-box; margin: 0; padding: 0; }
  html, body { width: 726px; height: 1200px; overflow: hidden; }
  body {
    background: var(--page);
    font-family: "Poppins", sans-serif;
    position: relative;
  }
  .sign {
    position: absolute;
    left: 18px; top: 248px;
    width: 690px; height: 704px;
    overflow: hidden;
    box-shadow: 0 14px 24px rgba(0,0,0,0.18);
  }
  .sign-bands { position: absolute; inset: 0; width: 690px; height: 704px; }
  .brand {
    position: absolute; left: 0; right: 0; top: 28px;
    display: flex; flex-direction: column; align-items: center;
  }
  .brand-dot {
    width: 168px; height: 168px; border-radius: 50%;
    background: var(--green);
  }
  .brand-name {
    margin-top: 18px;
    font-weight: 700; font-size: 42px; line-height: 1;
    letter-spacing: 1px; color: var(--black);
  }
  .brand-tagline {
    margin-top: 10px;
    font-weight: 500; font-size: 12.5px; letter-spacing: 6px;
    color: var(--green);
  }
  .service {
    position: absolute; top: 406px;
    width: 193px; height: 130px;
    background: var(--black); border-radius: 20px;
  }
  .service-arc {
    position: absolute; left: 8px; top: 8px; width: 40px; height: 100px;
  }
  .service-badge {
    position: absolute; left: 50%; top: -33px; transform: translateX(-50%);
    width: 78px; height: 78px; border-radius: 50%;
    background: var(--green);
    display: flex; align-items: center; justify-content: center;
  }
  .service-badge-inner {
    width: 64px; height: 64px; border-radius: 50%; background: var(--white);
    display: flex; align-items: center; justify-content: center;
  }
  .service-badge svg { width: 42px; height: 42px; }
  .service-title {
    position: absolute; left: 0; right: 0; top: 58px;
    text-align: center; color: var(--white);
    font-weight: 700; font-size: 22px; line-height: 27px;
  }
  .service--paving { left: 45px; }
  .service--fencing { left: 249px; }
  .service--design { left: 452px; }
  .contact { position: absolute; left: 165px; top: 596px; }
  .contact-row { display: flex; align-items: center; gap: 12px; }
  .contact-icon {
    width: 34px; height: 34px; border-radius: 7px; background: var(--black);
    display: flex; align-items: center; justify-content: center; flex: none;
  }
  .contact-icon svg { width: 22px; height: 22px; }
  .contact-phone { font-weight: 800; font-size: 46px; line-height: 54px; color: var(--black); letter-spacing: -0.5px; }
  .contact-row--email { margin-top: -2px; }
  .contact-row--email .contact-icon { width: 34px; height: 24px; border-radius: 5px; }
  .contact-email { font-weight: 700; font-size: 20px; line-height: 26px; color: var(--black); }
</style>
</head>
<body>
<main class="sign">
  <svg class="sign-bands" viewBox="0 0 690 704" aria-hidden="false">
    <defs>
      <linearGradient id="stoneTone" x1="0" y1="0" x2="1" y2="1">
        <stop offset="0" stop-color="#eeeeee"/>
        <stop offset="0.5" stop-color="#f5f5f5"/>
        <stop offset="1" stop-color="#e4e4e4"/>
      </linearGradient>
    </defs>
    <rect width="690" height="704" fill="url(#stoneTone)" role="img" aria-label="Pale grey stacked stone wall texture"/>
    <path class="band-edge" d="M0,258 Q345,442 690,236 L690,240 Q345,474 0,262 Z" fill="var(--black)"/>
    <path class="band-green" d="M0,262 Q345,474 690,240 L690,624 Q345,492 0,632 Z" fill="var(--green)"/>
    <path class="band-edge" d="M0,632 Q345,492 690,624 L690,652 Q345,485 0,683 Z" fill="var(--black)"/>
  </svg>

  <header class="brand">
    <div class="brand-dot"></div>
    <div class="brand-name">TERRACE RIDGE</div>
    <div class="brand-tagline">STRUCTURAL LANDSCAPING</div>
  </header>

  <section class="service service--paving">
    <svg class="service-arc" viewBox="0 0 40 100"><path d="M28,4 Q6,6 5,30 L5,96" fill="none" stroke="#fff" stroke-width="1.6"/></svg>
    <div class="service-badge"><div class="service-badge-inner">
      <svg viewBox="0 0 42 42" fill="none" stroke="#0b0b0b" stroke-width="2.4" stroke-linejoin="round">
        <ellipse cx="14" cy="15" rx="10" ry="7" transform="rotate(20 14 15)"/>
        <path d="M25 14 H33 L38 22 V30 H25 Z"/>
        <path d="M4 24 V30 H25"/>
        <circle cx="10" cy="32" r="3.5"/><circle cx="31" cy="32" r="3.5"/>
        <path d="M28 17 H32 L34 21 H28 Z"/>
      </svg>
    </div></div>
    <h2 class="service-title">PAVING &amp;<br>CONCRETING</h2>
  </section>

  <section class="service service--fencing">
    <svg class="service-arc" viewBox="0 0 40 100"><path d="M28,4 Q6,6 5,30 L5,96" fill="none" stroke="#fff" stroke-width="1.6"/></svg>
    <div class="service-badge"><div class="service-badge-inner">
      <svg viewBox="0 0 42 42" fill="none" stroke="#0b0b0b" stroke-width="2.4" stroke-linejoin="round">
        <path d="M5 12 L8 8 L11 12 V36 H5 Z"/>
        <path d="M15 10 L18 6 L21 10 V36 H15 Z"/>
        <path d="M25 10 L28 6 L31 10 V36 H25 Z"/>
        <path d="M34 12 L37 8 L40 12 V36 H34 Z"/>
        <path d="M11 16 H15 M21 16 H25 M31 16 H34 M11 28 H15 M21 28 H25 M31 28 H34"/>
      </svg>
    </div></div>
    <h2 class="service-title">FENCING &amp;<br>RETAINING</h2>
  </section>

  <section class="service service--design">
    <svg class="service-arc" viewBox="0 0 40 100"><path d="M28,4 Q6,6 5,30 L5,96" fill="none" stroke="#fff" stroke-width="1.6"/></svg>
    <div class="service-badge"><div class="service-badge-inner">
      <svg viewBox="0 0 42 42" fill="none" stroke="#0b0b0b" stroke-width="2.4" stroke-linejoin="round">
        <path d="M8 18 Q8 5 21 5 Q34 5 34 18"/>
        <path d="M17 5 V13 M25 5 V13"/>
        <path d="M5 18 H37 V22 H5 Z"/>
        <circle cx="21" cy="30" r="5"/>
        <path d="M11 24 L9 30 L12 33 L11 37 L16 36 L19 39 H23 L26 36 L31 37 L30 33 L33 30 L31 24"/>
      </svg>
    </div></div>
    <h2 class="service-title">DESIGN &amp;<br>CONSTRUCT</h2>
  </section>

  <footer class="contact">
    <div class="contact-row">
      <span class="contact-icon">
        <svg viewBox="0 0 24 24" fill="none" stroke="#fff" stroke-width="1.8" stroke-linecap="round" stroke-linejoin="round">
          <path d="M6 3 L9 7 L7.5 9.5 Q9.5 13.5 14 16 L16.5 14.5 L20.5 17.5 L18.5 20.5 Q10 20 4 11 Q3 6 6 3 Z"/>
          <path d="M14 4 Q19 5 20 10 M14 7.5 Q16.5 8 17 10.5"/>
        </svg>
      </span>
      <span class="contact-phone">0412 555 308</span>
    </div>
    <div class="contact-row contact-row--email">
      <span class="contact-icon">
        <svg viewBox="0 0 24 18" fill="none" stroke="#fff" stroke-width="2" stroke-linejoin="round">
          <rect x="3" y="3" width="18" height="12" rx="2"/>
          <path d="M3 4 L12 11 L21 4"/>
        </svg>
      </span>
      <span class="contact-email">sam@terraceridge.com</span>
    </div>
  </footer>
</main>
</body>
</html>
```